Banner Design

We need a banner to display at various locations around the community to promote our gymnastics club. Please see our plumivox page for more photos.

It should be horizontal 76cm X 183cm

```html
<!DOCTYPE html>
<html lang="en">
<head>
<meta charset="utf-8">
<title>Vaulta Gymsports Banner</title>
<link rel="stylesheet" href="https://fonts.googleapis.com/css2?family=Titan+One&family=Michroma&family=Montserrat:wght@600;800&display=swap">
<style>
  :root{
    --page:#d6d6d6;
    --paper:#ffffff;
    --green:#43a04a;
    --green-light:#8ed03f;
    --navy:#1e2a5e;
    --ink:#2b2f3a;
  }
  html,body{margin:0;padding:0;width:1200px;height:1200px;overflow:hidden;background:var(--page);}
  .canvas{position:relative;width:1200px;height:1200px;}
  .banner{position:absolute;left:0;top:172px;width:1200px;height:856px;display:block;}
  .brand-name{font-family:"Montserrat",sans-serif;font-weight:800;fill:var(--navy);}
  .headline{font-family:"Titan One",sans-serif;fill:var(--green);stroke:var(--navy);stroke-width:5;paint-order:stroke fill;stroke-linejoin:round;}
  .program{font-family:"Michroma",sans-serif;font-size:18.5px;fill:var(--ink);stroke:var(--ink);stroke-width:0.6;}
  .contact{font-family:"Montserrat",sans-serif;font-weight:600;font-size:12.5px;fill:#ffffff;letter-spacing:.4px;}
  .star{fill:var(--navy);}
</style>
</head>
<body>
<div class="canvas">
<svg class="banner" viewBox="0 0 1143 815" xmlns="http://www.w3.org/2000/svg">
  <defs>
    <symbol id="star" viewBox="-1 -1 2 2">
      <polygon points="0,-1 0.235,-0.324 0.951,-0.309 0.38,0.124 0.588,0.809 0,0.4 -0.588,0.809 -0.38,0.124 -0.951,-0.309 -0.235,-0.324"/>
    </symbol>
    <clipPath id="bannerClip"><rect width="1143" height="815"/></clipPath>
    <linearGradient id="photoMain" x1="0" y1="0" x2="0.35" y2="1">
      <stop offset="0" stop-color="#6a3a5e"/>
      <stop offset="0.2" stop-color="#b24a5a"/>
      <stop offset="0.42" stop-color="#c8455a"/>
      <stop offset="0.58" stop-color="#7b2f52"/>
      <stop offset="0.72" stop-color="#3a3f66"/>
      <stop offset="0.86" stop-color="#7fb842"/>
      <stop offset="1" stop-color="#26305a"/>
    </linearGradient>
    <linearGradient id="photoGym" x1="0" y1="0" x2="0" y2="1">
      <stop offset="0" stop-color="#7d6d5e"/>
      <stop offset="0.55" stop-color="#d26a9a"/>
      <stop offset="1" stop-color="#4f8a4a"/>
    </linearGradient>
    <linearGradient id="photoTeam" x1="0" y1="0" x2="0" y2="1">
      <stop offset="0" stop-color="#9a9ca3"/>
      <stop offset="0.5" stop-color="#3b4568"/>
      <stop offset="0.8" stop-color="#6fa73f"/>
      <stop offset="1" stop-color="#2a3550"/>
    </linearGradient>
  </defs>

  <rect width="1143" height="815" fill="var(--paper)"/>

  <g clip-path="url(#bannerClip)">
    <circle cx="862" cy="410" r="398" fill="var(--green)"/>
    <circle cx="872" cy="412" r="366" fill="#ffffff"/>
    <circle cx="876" cy="412" r="356" fill="var(--navy)"/>
    <circle cx="880" cy="412" r="344" fill="url(#photoMain)" role="img" aria-label="Photo: cheerleading team in green and navy uniforms performing a stunt at a state championship"/>

    <path d="M0,652 Q260,630 478,815 L0,815 Z" fill="var(--navy)"/>
    <path d="M0,660 Q252,642 462,815 L0,815 Z" fill="var(--green)"/>
  </g>

  <circle cx="522" cy="464" r="108" fill="#ffffff"/>
  <circle cx="522" cy="464" r="103" fill="url(#photoGym)" role="img" aria-label="Photo: young gymnast jumping in the gym"/>
  <circle cx="585" cy="618" r="98" fill="#ffffff"/>
  <circle cx="585" cy="618" r="93" fill="url(#photoTeam)" role="img" aria-label="Photo: cheer squad posing together"/>

  <text class="brand-name" x="292" y="118" font-size="74" text-anchor="middle" textLength="262" lengthAdjust="spacingAndGlyphs">VAULTA</text>
  <text class="brand-name" x="281" y="155" font-size="26" text-anchor="middle" letter-spacing="3">GYMSPORTS</text>

  <text class="headline" x="42" y="262" font-size="96" textLength="318" lengthAdjust="spacingAndGlyphs">Join in</text>
  <text class="headline" x="42" y="372" font-size="96" textLength="386" lengthAdjust="spacingAndGlyphs">The Fun</text>

  <g class="programs">
    <use class="star" href="#star" x="46" y="406" width="19" height="19"/>
    <text class="program" x="78" y="422">RECREATIONAL GYM</text>
    <use class="star" href="#star" x="46" y="436" width="19" height="19"/>
    <text class="program" x="78" y="452">COMPETITIVE GYM</text>
    <use class="star" href="#star" x="46" y="465" width="19" height="19"/>
    <text class="program" x="78" y="481">KINDER GYM</text>
    <use class="star" href="#star" x="46" y="494" width="19" height="19"/>
    <text class="program" x="78" y="510">BOYS PROGRAMS</text>
    <use class="star" href="#star" x="46" y="523" width="19" height="19"/>
    <text class="program" x="78" y="539">TUMBLING</text>
    <use class="star" href="#star" x="46" y="553" width="19" height="19"/>
    <text class="program" x="78" y="569">CHEERLEADING</text>
    <use class="star" href="#star" x="46" y="582" width="19" height="19"/>
    <text class="program" x="78" y="598">TRICKING</text>
    <use class="star" href="#star" x="46" y="611" width="19" height="19"/>
    <text class="program" x="78" y="627">PARKOUR</text>
  </g>

  <g class="contact-icons" fill="none" stroke="#ffffff" stroke-width="1.4">
    <path d="M52,692 a4,4 0 1 1 8,0 c0,3 -4,7 -4,7 c0,0 -4,-4 -4,-7z"/>
    <path d="M51,730 c1,-2 3,-2 4,0 l-1,2 c1,2 2,3 4,4 l2,-1 c2,1 2,3 0,4 c-5,1 -10,-4 -9,-9z"/>
    <rect x="51" y="752" width="10" height="8" rx="1.5"/>
    <path d="M51,753 l5,4 l5,-4"/>
    <circle cx="56" cy="779" r="5"/>
    <path d="M51,779 h10 M56,774 c-3,3 -3,7 0,10 M56,774 c3,3 3,7 0,10"/>
  </g>
  <text class="contact" x="70" y="700">42-44 Kestrel Lane,</text>
  <text class="contact" x="70" y="716">Marlow Bay, NSW, 2190</text>
  <text class="contact" x="70" y="739">(02) 5550 1827</text>
  <text class="contact" x="70" y="762">info@vaultagymsports.com</text>
  <text class="contact" x="70" y="785">www.vaultagymsports.com</text>

  <g class="star">
    <use href="#star" x="420" y="640" width="72" height="72"/>
    <use href="#star" x="498" y="698" width="44" height="44"/>
    <use href="#star" x="444" y="726" width="50" height="50"/>
    <use href="#star" x="560" y="742" width="30" height="30"/>
    <use href="#star" x="518" y="766" width="28" height="28"/>
    <use href="#star" x="602" y="770" width="22" height="22"/>
    <use href="#star" x="1024" y="28" width="22" height="22"/>
    <use href="#star" x="1038" y="46" width="36" height="36"/>
    <use href="#star" x="1086" y="52" width="28" height="28"/>
  </g>
</svg>
</div>
</body>
</html>
```